Business Cards Design for the electrical wholesaler: clean bold dynamic :)

We need a business card design that would follow our latest brand guidelines. As an electrical wholesaler we want to bring a fresh look and feel into the industry. The design should be clean bold and dynamic. It should come alive with the renewed energy of our green colour. Our grey colour should keep things balanced and complement the notion of maturity and responsibility. We employ Lato as a corporate font however are not bound by this font and we’re open to interpretation here.

Target Market(s)

Electrical contractors

Industry/Entity Type

Business

Contact Information for Business Card

Logo
Name & Surname: Olena Dovbush
Job Title: Director of Marketing
Email: helen.dovbush@mailvane.example
Cell phone: XXX.XXX.XXXX
Address: 20917 - 87 Ave. Edmonton, AB, Canada. T6K 2R8
Business Phone: 780.555.0187
Website: www.qorvil.example

Font styles to use
Other font styles liked:
• Lato

Requirements
Must have
• Logo & website
Nice to have
• Brand elements - some of them you may find in the attached Brand Guidelines (e.g. three lines on the background signifying "W")

```html
<!DOCTYPE html>
<html lang="en">
<head>
<meta charset="utf-8">
<title>QV Business Card – Design 2 Comp</title>
<link rel="stylesheet" href="https://fonts.googleapis.com/css2?family=Lato:wght@400;700;900&display=swap">
<style>
  :root {
    --page: #ffffff;
    --ink: #111111;
    --card-grey: #959595;
    --brand-orange: #f07106;
    --brand-grey: #4f4f4f;
    --brand-green: #8cc63f;
  }
  html, body {
    margin: 0;
    padding: 0;
    overflow: hidden;
    background: var(--page);
  }
  .board {
    position: relative;
    width: 1200px;
    height: 670px;
    overflow: hidden;
    background: var(--page);
    font-family: "Lato", sans-serif;
    color: var(--ink);
  }
  .board-title {
    position: absolute;
    left: 51px;
    top: 47px;
    margin: 0;
    font-size: 14.5px;
    font-weight: 400;
  }
  .card {
    position: absolute;
    top: 117px;
    width: 222px;
    height: 389px;
  }
  .card--front { left: 227px; background: var(--card-grey); }
  .card--back  { left: 684px; background: var(--brand-orange); }

  .brand {
    display: flex;
    align-items: center;
    gap: 8px;
    color: var(--brand-grey);
    font-weight: 700;
    line-height: 1;
    white-space: nowrap;
  }
  .brand-dot {
    display: block;
    border-radius: 50%;
    background: var(--brand-green);
    flex: none;
  }
  .card--front .brand {
    position: absolute;
    left: 12px;
    top: 44px;
    font-size: 46px;
  }
  .card--front .brand-dot { width: 34px; height: 34px; }

  .card--back .brand {
    position: absolute;
    left: 168px;
    top: 125px;
    font-size: 58px;
    transform: translate(-50%, -50%) rotate(-90deg);
  }
  .card--back .brand-dot { width: 40px; height: 40px; }

  .contact {
    position: absolute;
    left: 0;
    right: 0;
    text-align: center;
    padding-left: 14px;
  }
  .person { top: 124px; }
  .person-name {
    margin: 0;
    font-size: 20px;
    font-weight: 900;
    line-height: 1.1;
  }
  .person-role {
    margin: 2px 0 0;
    font-size: 12.5px;
    font-weight: 400;
    letter-spacing: 0.2px;
  }
  .phones {
    top: 188px;
    font-size: 15.5px;
    font-weight: 700;
    line-height: 21px;
  }
  .phones p, .email p { margin: 0; }
  .email {
    top: 240px;
    font-size: 12px;
    font-weight: 700;
  }
  .address {
    position: absolute;
    left: 18px;
    top: 297px;
    margin: 0;
    font-size: 12.8px;
    line-height: 13.6px;
    font-style: normal;
  }
  .website {
    position: absolute;
    left: 18px;
    top: 351px;
    margin: 0;
    font-size: 12.8px;
  }
  .card-label {
    position: absolute;
    top: 526px;
    margin: 0;
    transform: translateX(-50%);
    font-weight: 400;
  }
  .card-label--front { left: 326px; font-size: 14.5px; }
  .card-label--back  { left: 803px; font-size: 11.5px; letter-spacing: 1px; }
</style>
</head>
<body>
<main class="board">
  <h1 class="board-title">QV BUSINESS CARD - DESIGN 2 COMP</h1>

  <section class="card card--front" aria-label="Card front">
    <div class="brand"><span class="brand-dot"></span>qorvil</div>

    <div class="contact person">
      <p class="person-name">OLENA DOVBUSH</p>
      <p class="person-role">DIRECTOR OF MARKETING</p>
    </div>

    <div class="contact phones">
      <p>Cell: XXX.XXX.XXXX</p>
      <p>Office: 780.555.0187</p>
    </div>

    <div class="contact email">
      <p>helen.dovbush@mailvane.example</p>
    </div>

    <address class="address">20917 - 87 Avenue<br>Edmonton, AB, Canada<br>T6K 2R8</address>
    <p class="website">www.qorvil.example</p>
  </section>

  <section class="card card--back" aria-label="Card back">
    <div class="brand"><span class="brand-dot"></span>qorvil</div>
  </section>

  <p class="card-label card-label--front">FRONT</p>
  <p class="card-label card-label--back">BACK</p>
</main>
</body>
</html>
```